Online video and marketing company business cards

Need to get some new business cards designed to fit with our new logo. The cards should be professional, clean and simple.

Cards should have:

Name
Position
2 line address
telephone
mobile
email address
web address

We need to have our logo and if possible say what we do...
ONLINE FILM PRODUCTION & STRATEGY

Marketing

```html
<!DOCTYPE html>
<html lang="en">
<head>
<meta charset="utf-8">
<title>Lumareel Business Cards</title>
<link rel="stylesheet" href="https://fonts.googleapis.com/css2?family=Lato:wght@400;700&display=swap">
<style>
  :root {
    --page: #e4e2de;
    --card-blue: #5b8ea8;
    --navy: #1d4776;
    --card-light: #ebeced;
    --ink: #2b2b2b;
    --accent: #3f7fa6;
    --band: #5b8ea8;
  }
  * { margin: 0; padding: 0; box-sizing: border-box; }
  html, body { width: 1200px; height: 900px; overflow: hidden; }
  body {
    background: var(--page);
    font-family: "Lato", Arial, sans-serif;
    position: relative;
  }
  .card {
    position: absolute;
    width: 560px;
    height: 320px;
    left: 320px;
    box-shadow: 0 6px 18px rgba(0,0,0,0.15);
    overflow: hidden;
  }
  .card--front { top: 80px; background: var(--card-blue); }
  .card--back { top: 480px; background: var(--card-light); }

  .brand {
    display: flex;
    align-items: center;
    gap: 12px;
  }
  .brand__dot {
    width: 44px; height: 44px;
    border-radius: 50%;
    background: var(--navy);
    flex: none;
  }
  .brand__name {
    font-weight: 700;
    color: var(--navy);
    letter-spacing: -1px;
    line-height: 1;
  }

  .card--front .brand {
    position: absolute;
    left: 120px; top: 100px;
  }
  .card--front .brand__name { font-size: 64px; }
  .card--front .brand__dot { width: 56px; height: 56px; }
  .tagline {
    position: absolute;
    left: 0; right: 0; top: 228px;
    text-align: center;
    font-size: 17px;
    letter-spacing: 1.5px;
    color: var(--navy);
    text-transform: uppercase;
  }

  .card--back .brand {
    position: absolute;
    left: 34px; top: 56px;
  }
  .card--back .brand__name { font-size: 50px; }
  .contact {
    position: absolute;
    left: 40px; top: 142px;
    color: var(--ink);
  }
  .contact__name {
    font-size: 24px;
    margin-bottom: 10px;
  }
  .contact__role {
    font-size: 13px;
    color: var(--accent);
    letter-spacing: 1px;
    text-transform: uppercase;
    margin-left: 10px;
    vertical-align: 3px;
  }
  .contact__line {
    font-size: 15px;
    line-height: 24px;
  }
  .contact__label { color: var(--accent); font-weight: 700; margin-right: 6px; }
  .contact__sep { color: #888; margin: 0 8px; }
  .band {
    position: absolute;
    left: 0; right: 0; bottom: 0;
    height: 22px;
    background: var(--band);
  }
</style>
</head>
<body>
  <section class="card card--front" aria-label="Business card front">
    <div class="brand">
      <span class="brand__dot"></span>
      <span class="brand__name">lumareel</span>
    </div>
    <p class="tagline">Online Film Production &amp; Strategy</p>
  </section>

  <section class="card card--back" aria-label="Business card back">
    <div class="brand">
      <span class="brand__dot"></span>
      <span class="brand__name">lumareel</span>
    </div>
    <div class="contact">
      <p class="contact__name">Dana Kovren<span class="contact__role">Manager</span></p>
      <p class="contact__line"><span class="contact__label">T</span>555-201-3388<span class="contact__sep">|</span><span class="contact__label">M</span>555-118-2047</p>
      <p class="contact__line"><span class="contact__label">E</span>dana@lumareel.com<span class="contact__sep">|</span>www.lumareel.com</p>
      <p class="contact__line">18 Harbor Lane Suite 4, Brookfield NY 10020 USA</p>
    </div>
    <div class="band"></div>
  </section>
</body>
</html>
```